Choc biz start-up needs packaging design

We are a start-up chocolate company called 'Maison Verlaque Confections'. Our motto is 'Craft Beyond the Ordinary'. Themes associated with the company are: quality, social change, environmental awareness, innovation, refined and modern (with a strong emphasis on 'refined' - but not to the point of being boring!). Our product consists of bite-sized chocolate pieces. Being in the modern style, our products will utilise colour similar to www.tarvelbrookconfections.com, but with more restraint (that is, with a greater emphasis on the natural colours of chocolate: so the shades of white, milk and dark choc). We require a design for the exterior of both the LID and BASE.
More info:
---------------------------
Box shape and structure: See File 'cimg5416'
Logo: A logo has already been prepared, see 'AI-CMYK'. The main theme implied by this logo, is of 'nobility'. The style of lion itself is called a heraldic lion and traces back to European nobility. The colour of the logo is not fixed.
Product/Company info: See File 'back 3c', this text will need to go on the back of the box but how it appears is for you to decide
Dimensions (approx): note the length and width may vary but the height will stay at 33mm. This is because the design will be used for 9, 16 and 25 piece boxes.
Of entire box: 150mm x 150mm x 33mm high
Of lid: 150mm x 150mm x 23mm high (note this means that the base will be visible from the sides, when the box is closed)
Colours to avoid: large amounts of black and/or white
Colours to use: branding colours not yet determined so the designer is welcome to use any colours that s/he wishes.
File format: will require file to eventually be provided in vector format
Other: packaging will be CMYK printed and can be either matte/gloss laminated. To reduce costs, there will be no heat-stamping/embossing/etc.
Thoughts on other choc packaging:
File named '626808': Nice, but a little too plain and static (for what I'm after).
File named 'index3': Nice, but too traditional (for what I'm after).
File named 'imagesc': Nice, a little too modern and simple (for what I'm after). To me, it doesn't say refined enough.
File named '12cm cover colour a': This was the design that I'd been working on. But I'm not a graphic designer, it looks incomplete and I feel that it's incorporating elements potentially too ornate to incorporate into the overall company branding. I'm just as likely to choose an all-new design that I like than to pick one that improves upon what I'd started (assuming the issues I had with the design are also addressed).
Updates
For those who read the brief on the 6th of July, or earlier:
It's come to my attention that the file numbers referred to in the brief did not match the file numbers that I uploaded (PixelGuild somehow jumbled it all up). I've since edited the brief to make references to the file names and not numbers. My apologies for any confusion caused.
Industry/Entity Type
Chocolate Company
Look and feel
Each slider illustrates characteristics of the customer's brand and the style your logo design should communicate.

```html
<!DOCTYPE html>
<html lang="en">
<head>
<meta charset="utf-8">
<title>Maison Verlaque Confections — Lid Design</title>
<link rel="stylesheet" href="https://fonts.googleapis.com/css2?family=Libre+Baskerville:wght@400;700&display=swap">
<style>
  :root {
    --page-bg: #ffffff;
    --plum: #5b1a5e;
    --plum-deep: #4a1250;
    --plum-swirl: #66256a;
    --gold: #c9a56b;
    --gold-light: #dcbf8a;
    --frame-line: rgba(201, 165, 107, 0.45);
  }
  * { margin: 0; padding: 0; box-sizing: border-box; }
  html, body {
    width: 710px;
    height: 1200px;
    overflow: hidden;
    background: var(--page-bg);
  }
  .canvas {
    position: relative;
    width: 710px;
    height: 1200px;
    display: flex;
    align-items: center;
    justify-content: center;
  }
  .lid {
    position: relative;
    width: 590px;
    height: 590px;
    background: var(--plum);
    overflow: hidden;
  }
  .lid__swirl-pattern {
    position: absolute;
    inset: 0;
    background:
      radial-gradient(circle at 70% 30%, var(--plum-swirl) 0%, transparent 45%),
      radial-gradient(circle at 30% 80%, var(--plum-swirl) 0%, transparent 40%),
      linear-gradient(160deg, var(--plum) 0%, var(--plum-deep) 100%);
  }
  .lid__frame {
    position: absolute;
    inset: 36px;
    border: 1px solid var(--frame-line);
  }
  .lid__ribbon {
    position: absolute;
    top: 0;
    bottom: 0;
    left: 143px;
    width: 70px;
    background: linear-gradient(90deg, var(--gold) 0%, var(--gold-light) 50%, var(--gold) 100%);
    opacity: 0.85;
  }
  .brand-seal {
    position: absolute;
    left: 178px;
    top: 232px;
    transform: translate(-50%, -50%);
    width: 108px;
    height: 108px;
    border-radius: 50%;
    background: var(--plum);
    border: 2px solid var(--gold);
    display: flex;
    align-items: center;
    justify-content: center;
    text-align: center;
    padding: 12px;
  }
  .brand-seal__name {
    font-family: 'Libre Baskerville', Georgia, serif;
    font-weight: 700;
    font-size: 11px;
    line-height: 1.35;
    color: var(--gold);
    letter-spacing: 0.5px;
  }
  .lid__tagline {
    position: absolute;
    right: 48px;
    bottom: 60px;
    font-family: 'Libre Baskerville', Georgia, serif;
    font-weight: 700;
    font-size: 17px;
    color: var(--gold);
    letter-spacing: 0.2px;
  }
</style>
</head>
<body>
  <main class="canvas">
    <section class="lid">
      <div class="lid__swirl-pattern" role="img" aria-label="Tonal plum swirl flourish pattern across the lid"></div>
      <div class="lid__frame"></div>
      <div class="lid__ribbon" role="img" aria-label="Vertical gold band of interlocking diamond ornaments"></div>
      <div class="brand-seal">
        <span class="brand-seal__name">Maison Verlaque Confections</span>
      </div>
      <p class="lid__tagline">Craft Beyond the Ordinary</p>
    </section>
  </main>
</body>
</html>
```